Brightmoor Vector Systems Website

I am starting an IT consulting business called Brightmoor Vector Systems. I recently completed a logo contest on ArtHive and am now looking to put together a basic website. I can provide text and content but am looking for a site design with layout and graphics. I am attaching my logo below. I was thinking of a dark blue and white theme for the website (similar to the logo). However, I am open to ideas. Graphics can be a mix of business and high tech as that is the image I am trying to convey. The site will be relatively simple and probably have only 3 - 5 pages (Home, About Us, Services, Contact, etc.)
Target Market(s)
United States commercial companies and government contractors
Industry/Entity Type
Consulting

```html
<!DOCTYPE html>
<html lang="en">
<head>
<meta charset="utf-8">
<title>Brightmoor Vector Systems</title>
<link href="https://fonts.googleapis.com/css2?family=Mulish:wght@400;600;700;800&family=Teko:wght@300;400&display=swap" rel="stylesheet">
<style>
:root{
  --blue:#0b74c8;
  --blue-dark:#075ea6;
  --navy:#1f2540;
  --ink:#1d1f2a;
  --muted:#555a66;
  --line:#e3e6ec;
  --grey:#f2f3f5;
  --white:#ffffff;
}
*{margin:0;padding:0;box-sizing:border-box}
html,body{width:1200px;height:4274px;overflow:hidden;background:var(--white)}
body{font-family:"Mulish",Arial,sans-serif;color:var(--ink);position:relative}
.abs{position:absolute}
.btn{position:absolute;display:flex;align-items:center;justify-content:center;border-radius:20px;font-size:12px;font-weight:700;text-decoration:none}
.btn-blue{background:var(--blue);color:var(--white)}
.btn-white{background:var(--white);color:var(--blue)}
.btn-outline-blue{border:1.5px solid var(--blue);color:var(--blue);background:var(--white)}
.btn-outline-white{border:1.5px solid var(--white);color:var(--white)}
.brand{display:flex;align-items:center;gap:8px;font-weight:800;color:var(--navy);letter-spacing:1px}
.brand-dot{width:14px;height:14px;border-radius:50%;background:var(--blue)}

/* header */
.site-header{position:absolute;left:0;top:0;width:1200px;height:80px;background:var(--white);z-index:5}
.site-header .brand{position:absolute;left:88px;top:24px;font-size:18px}
.nav{position:absolute;left:434px;top:32px;display:flex;gap:22px;font-size:12px;font-weight:600}
.nav a{color:var(--ink);text-decoration:none}
.nav a.active{color:var(--blue)}
.call{position:absolute;left:805px;top:32px;font-size:13px;font-weight:700;color:var(--blue)}

/* hero */
.hero-title{left:88px;top:222px;width:440px;font-size:39px;line-height:46px;font-weight:800;color:var(--white)}
.section-title{position:absolute;left:0;width:1200px;text-align:center;font-size:29px;font-weight:800;color:var(--blue)}
.section-lead{position:absolute;left:0;width:1200px;text-align:center;font-size:12px;line-height:19px;color:var(--muted)}

/* services */
.service-card{position:absolute;top:945px;width:320px;height:247px;background:var(--white);border:1px solid var(--line);text-align:center}
.service-card.raised{box-shadow:0 6px 22px rgba(20,30,60,.12);border-color:transparent}
.service-icon{position:absolute;left:112px;top:-48px;width:96px;height:96px;border-radius:50%;background:var(--white);border:1px solid var(--line);display:flex;align-items:center;justify-content:center}
.service-card h3{margin-top:68px;font-size:18px;font-weight:700}
.service-card p{margin:14px 28px 0;font-size:11.5px;line-height:19px;color:var(--muted)}
.read-more{display:inline-block;margin-top:12px;font-size:12px;font-weight:700;color:var(--blue)}

/* feature band */
.feature-title{left:641px;top:1475px;font-size:28px;font-weight:800;color:var(--white)}
.feature-copy{left:641px;top:1538px;width:475px;font-size:12.5px;line-height:17px;font-weight:600;color:var(--white)}
.feature-copy p+p{margin-top:17px}
.why-title{left:88px;top:1783px;font-size:28px;font-weight:800;color:var(--white)}
.why-item{position:absolute;left:88px;display:flex;align-items:center;gap:34px;color:var(--white);font-size:13.5px;line-height:20px;font-weight:600}
.why-icon{width:78px;height:66px;flex:none}
.wordmark{left:660px;top:2150px;color:var(--navy);text-align:left}
.wordmark .name{display:flex;align-items:center;gap:14px;font-size:46px;font-weight:800;letter-spacing:2px}
.wordmark .name .brand-dot{width:40px;height:40px}
.wordmark .sub{margin-top:6px;font-size:18px;letter-spacing:18px;font-weight:800;padding-left:54px}

/* stats */
.stat{position:absolute;top:2308px;width:240px;text-align:center}
.stat-icon{margin:0 auto;width:80px;height:80px;border-radius:50%;background:var(--white);box-shadow:0 4px 16px rgba(20,30,60,.08);display:flex;align-items:center;justify-content:center}
.stat-num{margin-top:14px;font-family:"Teko",sans-serif;font-weight:300;font-size:44px;line-height:40px;color:var(--blue)}
.stat-label{margin-top:4px;font-size:15px;font-weight:600;color:var(--ink)}

/* news */
.news-card{position:absolute;top:2757px;width:320px;height:396px;background:var(--white);box-shadow:0 4px 18px rgba(20,30,60,.07);border-bottom:4px solid var(--blue)}
.news-card.soft{border-bottom-color:#7fb2df}
.news-photo{height:200px}
.news-body{padding:28px 32px}
.news-date{font-size:13px;font-weight:700;color:var(--blue)}
.news-title{margin-top:14px;font-size:17px;line-height:22px;font-weight:600;color:var(--ink)}
.news-more{margin-top:28px;font-size:12.5px;font-weight:700;color:var(--blue);display:flex;align-items:center;gap:14px}
.news-more .chev{width:28px;height:28px;border-radius:50%;background:var(--blue);display:flex;align-items:center;justify-content:center}

/* estimate form */
.field{position:absolute;border:1px solid var(--line);border-radius:16px;font-size:11px;color:var(--muted);padding:8px 16px}

/* cta + footer */
.cta-title{left:88px;top:3793px;width:700px;font-size:29px;line-height:37px;font-weight:800;color:var(--white)}
.site-footer{position:absolute;left:0;top:3900px;width:1200px;height:374px;background:var(--navy);color:var(--white)}
.footer-col{position:absolute;top:68px}
.footer-col h4{font-size:18px;font-weight:800;margin-bottom:16px}
.footer-col p,.footer-col li{font-size:12px;line-height:19px}
.footer-col ul{list-style:none}
.footer-col li{line-height:24px}
.newsletter-input{margin-top:16px;width:232px;height:30px;border-radius:16px;background:var(--white);color:var(--ink);font-size:11px;padding:8px 16px}
.footer-rule{position:absolute;left:88px;top:300px;width:1024px;height:1px;background:rgba(255,255,255,.2)}
.copyright{position:absolute;left:88px;top:332px;font-size:11.5px}
.copyright span{color:var(--blue)}
.socials{position:absolute;left:880px;top:324px;display:flex;gap:10px}
.socials i{width:30px;height:30px;border-radius:50%;border:1.5px solid var(--blue)}
.socials i.on{background:var(--blue)}
</style>
</head>
<body>

<header class="site-header">
  <div class="brand"><span class="brand-dot"></span>BRIGHTMOOR VECTOR</div>
  <nav class="nav">
    <a class="active" href="#">Home</a><a href="#">About Us</a><a href="#">Services</a><a href="#">Blog</a><a href="#">Contact Us</a>
  </nav>
  <div class="call">Call Us: +555-014-2290</div>
  <a class="btn btn-blue" style="left:983px;top:24px;width:128px;height:32px">Get a Quote</a>
</header>

<!-- hero -->
<svg class="abs" style="left:0;top:80px" width="1200" height="660" viewBox="0 0 1200 660">
  <defs>
    <linearGradient id="heroPhoto" x1="0" y1="0" x2="1" y2="1">
      <stop offset="0" stop-color="#3c4a78"/><stop offset="1" stop-color="#6a7cae"/>
    </linearGradient>
    <radialGradient id="heroArt" cx=".5" cy=".5" r=".5">
      <stop offset="0" stop-color="#f0f0fb"/><stop offset="1" stop-color="#dcdcf4"/>
    </radialGradient>
  </defs>
  <polygon points="0,0 1200,0 1200,290 320,647 0,490" fill="#0b74c8"/>
  <polygon points="0,0 1200,0 1200,290 320,635 0,480" fill="url(#heroPhoto)" role="img" aria-label="Photo of a business team meeting with a dark blue overlay"/>
  <polygon points="1200,290 860,440 1200,440" fill="#ffffff"/>
  <circle cx="863" cy="352" r="238" fill="url(#heroArt)" role="img" aria-label="Illustration of a consultant presenting charts to two colleagues at laptops"/>
</svg>
<h1 class="abs hero-title">Brightmoor Vector is a management and technology consulting company</h1>
<a class="btn btn-white" style="left:88px;top:442px;width:128px;height:32px">Contact Us</a>

<!-- services -->
<h2 class="section-title" style="top:784px">Service we provide</h2>
<p class="section-lead" style="top:832px">Lorem Ipsum is simply dummy text of the printing and typesetting industry.<br>lorem Ipsum has been the industry's standard dummy</p>

<div class="service-card" style="left:88px">
  <div class="service-icon"><svg width="44" height="44" viewBox="0 0 44 44" fill="none" stroke="#1f2540" stroke-width="2"><circle cx="22" cy="14" r="6"/><path d="M10 36c0-7 5-11 12-11s12 4 12 11"/><circle cx="8" cy="20" r="3"/><circle cx="36" cy="20" r="3"/></svg></div>
  <h3>Staff Augmentation</h3>
  <p>It is a long established fact that a reader will be distracted by the readable content of a page when looking at its layout. The point of using lorem Ipsum is that it normal ...</p>
  <span class="read-more">Read More &nbsp;→</span>
</div>
<div class="service-card raised" style="left:440px">
  <div class="service-icon"><svg width="44" height="44" viewBox="0 0 44 44" fill="none" stroke="#1f2540" stroke-width="2"><rect x="6" y="6" width="32" height="14" rx="2" stroke="#0b74c8"/><circle cx="14" cy="28" r="4"/><circle cx="30" cy="28" r="4"/><path d="M6 40c0-5 4-7 8-7s8 2 8 7M22 40c0-5 4-7 8-7s8 2 8 7"/></svg></div>
  <h3>Consulting</h3>
  <p>It is a long established fact that a reader will be distracted by the readable content of a page when looking at its layout. The point of using lorem Ipsum is that it normal ...</p>
  <span class="read-more">Read More &nbsp;→</span>
</div>
<div class="service-card" style="left:793px">
  <div class="service-icon"><svg width="44" height="44" viewBox="0 0 44 44" fill="none" stroke="#1f2540" stroke-width="2"><rect x="8" y="16" width="28" height="20" rx="2"/><path d="M16 16v-4h12v4M8 26h28"/><circle cx="22" cy="8" r="3" stroke="#0b74c8"/></svg></div>
  <h3>Managed Services</h3>
  <p>It is a long established fact that a reader will be distracted by the readable content of a page when looking at its layout. The point of using lorem Ipsum is that it normal ...</p>
  <span class="read-more">Read More &nbsp;→</span>
</div>
<a class="btn btn-outline-blue" style="left:520px;top:1232px;width:160px;height:32px">View All Services</a>

<!-- feature band -->
<svg class="abs" style="left:0;top:1255px" width="1200" height="1302" viewBox="0 0 1200 1302">
  <defs>
    <linearGradient id="techPhoto" x1="0" y1="0" x2="1" y2="1">
      <stop offset="0" stop-color="#c9d6e6"/><stop offset=".55" stop-color="#4f6c94"/><stop offset="1" stop-color="#c4763a"/>
    </linearGradient>
  </defs>
  <rect width="1200" height="1302" fill="#ffffff"/>
  <polygon points="0,880 1200,620 1200,1302 0,1302" fill="#f2f3f5"/>
  <polygon points="0,212 996,0 1200,30 1200,797 204,1004 0,896" fill="#1f2540"/>
  <polygon points="0,896 204,1004 232,995 0,880" fill="#0b74c8"/>
  <polygon points="1004,13 1200,40 1200,797 480,457 548,180" fill="#0b74c8"/>
  <circle cx="335" cy="264" r="221" fill="#ffffff"/>
  <circle cx="335" cy="264" r="179" fill="url(#techPhoto)" role="img" aria-label="Photo of a hand drawing business charts on a digital screen"/>
</svg>
<h2 class="abs feature-title">Brightmoor Vector Systems</h2>
<div class="abs feature-copy">
  <p>There are many variations of passages of Lorem Ipsum available, but the majority have suffered alteration in some form, by injected humour, or randomised words which don't look even slightly believable. If you are going to use a passage of Lorem Ipsum.</p>
  <p>All the Lorem Ipsum generators on the Internet tend to repeat predefined chunks as necessary, making this the first true generator ...</p>
</div>
<a class="btn btn-outline-white" style="left:641px;top:1696px;width:128px;height:32px">About Us</a>

<h2 class="abs why-title">Why choose us</h2>
<div class="why-item" style="top:1848px">
  <svg class="why-icon" viewBox="0 0 78 66" fill="none"><path d="M4 33 22 3h36l16 30-16 30H22Z" stroke="#3a4668" stroke-width="1.5"/><rect x="31" y="22" width="16" height="20" rx="2" stroke="#0b74c8" stroke-width="2"/><path d="M35 32l3 3 5-6" stroke="#0b74c8" stroke-width="2"/></svg>
  <span>There are many variations of passages of lorem<br>Ipsum available, but the majority</span>
</div>
<div class="why-item" style="top:1928px">
  <svg class="why-icon" viewBox="0 0 78 66" fill="none"><path d="M4 33 22 3h36l16 30-16 30H22Z" stroke="#3a4668" stroke-width="1.5"/><circle cx="32" cy="28" r="4" stroke="#0b74c8" stroke-width="2"/><circle cx="46" cy="28" r="4" stroke="#0b74c8" stroke-width="2"/><path d="M24 42c0-5 4-8 8-8s8 3 8 8M38 42c0-5 4-8 8-8s8 3 8 8" stroke="#0b74c8" stroke-width="2"/></svg>
  <span>There are many variations of passages of lorem<br>Ipsum available, but the majority</span>
</div>
<div class="why-item" style="top:2008px">
  <svg class="why-icon" viewBox="0 0 78 66" fill="none"><path d="M4 33 22 3h36l16 30-16 30H22Z" stroke="#3a4668" stroke-width="1.5"/><circle cx="39" cy="33" r="12" fill="#0b74c8"/><path d="M27 33h24M39 21v24" stroke="#1f2540" stroke-width="1.5"/></svg>
  <span>There are many variations of passages of lorem<br>Ipsum available, but the majority</span>
</div>
<a class="btn btn-white" style="left:88px;top:2104px;width:128px;height:32px">Get a Quote</a>

<div class="abs wordmark">
  <div class="name"><span class="brand-dot"></span>BRIGHTMOOR</div>
  <div class="sub">VECTOR SYSTEMS</div>
</div>

<!-- stats -->
<div class="stat" style="left:66px">
  <div class="stat-icon"><svg width="30" height="30" viewBox="0 0 30 30" fill="none" stroke="#0b74c8" stroke-width="2"><path d="M4 13h5v13H4zM9 14l6-10c2 0 3 2 2 5l-1 4h8c2 0 3 2 2 4l-3 8c-1 2-2 2-4 2H9"/></svg></div>
  <div class="stat-num">21+</div><div class="stat-label">Years of experience</div>
</div>
<div class="stat" style="left:341px">
  <div class="stat-icon"><svg width="34" height="30" viewBox="0 0 34 30" fill="none" stroke="#0b74c8" stroke-width="2"><path d="M2 16l7 7L24 6M12 20l3 3L32 6"/></svg></div>
  <div class="stat-num">100+</div><div class="stat-label">Projects completed</div>
</div>
<div class="stat" style="left:617px">
  <div class="stat-icon"><svg width="34" height="30" viewBox="0 0 34 30" fill="none" stroke="#0b74c8" stroke-width="2"><circle cx="12" cy="10" r="5"/><circle cx="23" cy="10" r="5"/><path d="M3 26c0-6 4-9 9-9s9 3 9 9M18 18c1-1 3-1 5-1 5 0 9 3 9 9"/></svg></div>
  <div class="stat-num">500+</div><div class="stat-label">Qualified team member</div>
</div>
<div class="stat" style="left:894px">
  <div class="stat-icon"><svg width="30" height="34" viewBox="0 0 30 34" fill="none" stroke="#0b74c8" stroke-width="2"><path d="M15 2v30M22 9c-1-2-4-3-7-3-4 0-7 2-7 5 0 7 14 4 14 11 0 3-3 5-7 5-3 0-6-1-7-4"/></svg></div>
  <div class="stat-num">$30M</div><div class="stat-label">Annual revenue</div>
</div>

<!-- news -->
<h2 class="section-title" style="top:2630px">News &amp; updates</h2>
<p class="section-lead" style="top:2678px">Lorem ipsum dolor sit amet, consectetur adipiscing elit, sed do eiusmod<br>tempor incididunt ut labore et dolore magna aliqua.</p>

<article class="news-card" style="left:88px">
  <div class="news-photo" role="img" aria-label="Photo of a businesswoman with a tablet and cloud technology graphics" style="background:linear-gradient(135deg,#e7ebf0,#9aa9bb)"></div>
  <div class="news-body">
    <div class="news-date">Mar 29, 2021</div>
    <div class="news-title">It is a long established fact reader will be distracted by the readable content</div>
    <div class="news-more">Read More <span class="chev"><svg width="10" height="10" viewBox="0 0 10 10" fill="none" stroke="#fff" stroke-width="1.8"><path d="M3 1l4 4-4 4"/></svg></span></div>
  </div>
</article>
<article class="news-card soft" style="left:440px">
  <div class="news-photo" role="img" aria-label="Photo of colleagues talking around a meeting table" style="background:linear-gradient(135deg,#b07a5a,#4c4a52)"></div>
  <div class="news-body">
    <div class="news-date">Mar 29, 2021</div>
    <div class="news-title">It is a long established fact reader will be distracted by the readable content</div>
    <div class="news-more" style="margin-top:33px">Read More <span style="font-size:14px">›</span></div>
  </div>
</article>
<article class="news-card soft" style="left:793px">
  <div class="news-photo" role="img" aria-label="Photo of a hand holding a glowing light bulb with gear graphics" style="background:linear-gradient(135deg,#3a3f48,#8d8f93)"></div>
  <div class="news-body">
    <div class="news-date">Mar 29, 2021</div>
    <div class="news-title">It is a long established fact reader will be distracted by the readable content</div>
    <div class="news-more" style="margin-top:33px">Read More <span style="font-size:14px">›</span></div>
  </div>
</article>
<a class="btn btn-outline-blue" style="left:536px;top:3197px;width:128px;height:32px">View All News</a>

<!-- estimate -->
<h2 class="section-title" style="top:3302px">Get a free estimate</h2>
<div class="field" style="left:208px;top:3372px;width:247px;height:30px">Your Name</div>
<div class="field" style="left:476px;top:3372px;width:247px;height:30px">Email</div>
<div class="field" style="left:745px;top:3372px;width:247px;height:30px">Phone</div>
<div class="field" style="left:208px;top:3424px;width:784px;height:106px;border-radius:10px;padding:14px 16px">Message ...</div>
<a class="btn btn-blue" style="left:553px;top:3546px;width:96px;height:32px">Submit</a>

<!-- call to action -->
<svg class="abs" style="left:0;top:3655px" width="1200" height="246" viewBox="0 0 1200 246">
  <polygon points="0,88 400,0 1200,110 1200,246 0,246" fill="#1f2540"/>
  <polygon points="0,98 400,14 1200,118 1200,246 0,246" fill="#0b74c8"/>
  <rect x="156" y="6" width="114" height="106" rx="10" fill="#3b8fd6" role="img" aria-label="Line icon of a gear with people and a handshake"/>
</svg>
<h2 class="abs cta-title">Brightmoor Vector Systems is always looking for the best and brightest</h2>
<a class="btn btn-outline-white" style="left:880px;top:3822px;width:232px;height:32px">Start Work With Brightmoor</a>

<!-- footer -->
<footer class="site-footer">
  <div class="brand" style="position:absolute;left:88px;top:74px;color:#fff;font-size:17px"><span class="brand-dot"></span>BRIGHTMOOR VECTOR</div>
  <div class="footer-col" style="left:352px">
    <h4>Contact Us</h4>
    <p style="font-size:16px">Call Us: +1555-014-2290</p>
    <p><b>e.</b> info@brightmoorvector.com</p>
    <p style="margin-top:22px"><b>Address:</b><br>4410 Harbor Ridge Parkway, Dalton,<br>GA 30720</p>
  </div>
  <div class="footer-col" style="left:680px">
    <h4>Quick Links</h4>
    <ul><li>Home</li><li>About Us</li><li>Services</li><li>Blog</li><li>Careers</li><li>Contact Us</li></ul>
  </div>
  <div class="footer-col" style="left:878px">
    <h4>Sign Up Newsletter</h4>
    <p>There are many variations of passages<br>lorem Ipsum available</p>
    <div class="newsletter-input">Enter your email ...</div>
    <a class="btn btn-blue" style="position:relative;display:flex;margin-top:10px;width:96px;height:30px">Send</a>
  </div>
  <div class="footer-rule"></div>
  <div class="copyright">© 2021 <span>Brightmoor Vector Systems</span>. All Right Reserved</div>
  <div class="socials"><i></i><i class="on"></i><i></i><i></i></div>
</footer>

</body>
</html>
```